Personal Training Business Card Design

I have just started my own personal training business called "Lana Corvell Fitness". My goal as a personal trainer is to motivate, inspire and educate all of my clients about the benefits of regular exercise, nourishing the body with nutritious foods and living healthy. I train both men and women, so I would like a business card that will appeal to both sexes and not come across too feminine or too masculine. I'm looking for a fresh, yet simple look which uses "fresh" colours such as green, white and grey - similar to my logo (but open to other effective gender-neutral colour schemes). I am open to using the logo I have uploaded as one image together, or separating the text and image (also supplied).
Industry/Entity Type
Personal Trainer
Contact Information for Business Card
Lana Corvell
Fitness Coach
Address: Ground Floor, Maplewick House, 342 Larkin St, Brisbane City, 4000
Email: lanacorvellfitness@mailorbit.net
Phone: 0455 293 604
Facebook: www.socialnook.net/lanacorvellfitness
Look and feel

```html
<!DOCTYPE html>
<html lang="en">
<head>
<meta charset="utf-8">
<title>Lana Corvell Fitness – Business Card</title>
<link href="https://fonts.googleapis.com/css2?family=Questrial&family=Roboto:wght@300;400&display=swap" rel="stylesheet">
<style>
  :root {
    --green: #8cc63f;
    --green-dark: #6ea82a;
    --green-light: #a9d86a;
    --grey-text: #8a8a8a;
    --grey-dark: #6f6f6f;
    --card-white: #fbfbfb;
    --canvas: #dcdcdc;
  }
  * { margin: 0; padding: 0; box-sizing: border-box; }
  html, body {
    width: 1200px; height: 1023px; overflow: hidden;
    background: var(--canvas);
  }
  .canvas {
    position: relative; width: 1200px; height: 1023px;
    display: flex; flex-direction: column; align-items: center;
    justify-content: center; gap: 44px;
  }
  .card {
    position: relative; width: 805px; height: 460px;
    box-shadow: 0 6px 18px rgba(0,0,0,.18);
    overflow: hidden;
  }
  .card-front {
    background: linear-gradient(135deg, #ffffff 0%, var(--card-white) 55%, #eeeeee 100%);
  }
  .front-band {
    position: absolute; left: 0; right: 0; bottom: 0; height: 56px;
    background: linear-gradient(90deg, var(--green-light), var(--green) 60%, var(--green-dark));
  }
  .brand {
    position: absolute; right: 70px; top: 48px; width: 320px;
    display: flex; flex-direction: column; align-items: flex-end;
  }
  .brand-mark {
    width: 118px; height: 118px; border-radius: 50%;
    background: var(--green); margin-right: 90px;
  }
  .brand-name {
    margin-top: 40px;
    font-family: "Questrial", sans-serif; font-size: 25px;
    letter-spacing: 1px; color: var(--green); white-space: nowrap;
  }
  .brand-tagline {
    margin-top: 2px;
    font-family: "Roboto", sans-serif; font-weight: 300;
    font-size: 19px; letter-spacing: 1.5px; color: var(--grey-text);
    white-space: nowrap;
  }
  .person {
    position: absolute; left: 58px; top: 138px;
  }
  .person-name {
    font-family: "Questrial", sans-serif; font-weight: 400; font-size: 33px;
    color: var(--green); line-height: 1;
  }
  .person-title {
    font-family: "Roboto", sans-serif; font-weight: 400;
    font-size: 18px; color: var(--grey-dark); margin-top: 4px;
  }
  .contact-list {
    list-style: none; margin-top: 16px;
    font-family: "Roboto", sans-serif; font-weight: 300;
    font-size: 15px; line-height: 1.3; color: var(--grey-text);
  }
  .contact-list li { margin-bottom: 7px; white-space: nowrap; }
  .contact-list li:last-child { margin-bottom: 0; }
  .contact-icon {
    display: inline-block; width: 14px; height: 14px;
    vertical-align: -2px; margin-left: 6px;
  }
  .card-back {
    background: linear-gradient(135deg, var(--green-light) 0%, var(--green) 50%, var(--green-dark) 100%);
  }
</style>
</head>
<body>
<main class="canvas">
  <section class="card card-front">
    <div class="brand">
      <div class="brand-mark"></div>
      <div class="brand-name">LANA CORVELL FITNESS</div>
      <div class="brand-tagline">motivate. inspire. educate.</div>
    </div>

    <div class="person">
      <h1 class="person-name">Lana Corvell</h1>
      <p class="person-title">Fitness Coach</p>
      <ul class="contact-list">
        <li>0455 293 604
          <svg class="contact-icon" viewBox="0 0 16 16" aria-hidden="true"><path fill="#8cc63f" d="M3.6 1.5l2.3 0 1 3.2-1.6 1.2c.8 1.8 2.1 3.1 3.9 3.9l1.2-1.6 3.2 1v2.3c0 .9-.8 1.6-1.7 1.5C6.6 12.6 3.4 9.4 2 4.1c-.1-.9.6-2.6 1.6-2.6z"/></svg>
        </li>
        <li>Ground Floor, Maplewick House,
          <svg class="contact-icon" viewBox="0 0 16 16" aria-hidden="true"><path fill="#8cc63f" d="M8 1.5L1 8h2v6h4v-4h2v4h4V8h2z"/></svg><br>342 Larkin St, Brisbane City, 4000
        </li>
        <li>www.socialnook.net
          <svg class="contact-icon" viewBox="0 0 16 16" aria-hidden="true"><g fill="none" stroke="#8cc63f" stroke-width="1.6"><circle cx="8" cy="8" r="6.2"/><path d="M1.8 8h12.4M8 1.8c-2.4 3.4-2.4 9 0 12.4M8 1.8c2.4 3.4 2.4 9 0 12.4"/></g></svg><br>/lanacorvellfitness
        </li>
        <li>lanacorvellfitness@mailorbit.net
          <svg class="contact-icon" viewBox="0 0 16 16" aria-hidden="true"><rect x="1" y="3" width="14" height="10" rx="1" fill="#8cc63f"/><path d="M1.5 3.6L8 9l6.5-5.4" fill="none" stroke="#fff" stroke-width="1.3"/></svg>
        </li>
      </ul>
    </div>

    <div class="front-band"></div>
  </section>

  <section class="card card-back" aria-label="Card reverse, solid green"></section>
</main>
</body>
</html>
```